Slide desk development crimson ledge holdings

I am looking to expand the range of slide templates we have using our new branded powerpoint deck so the team have more options.

Target Market(s)

We operate in the construction sector

Industry/Entity Type

Construction

Requirements
Must have
• Picture linking back to construction

```html
<!DOCTYPE html>
<html lang="en">
<head>
<meta charset="utf-8">
<title>Icons to use</title>
<link rel="stylesheet" href="https://fonts.googleapis.com/css2?family=Poppins:wght@700&display=swap">
<style>
  :root {
    --paper: #ffffff;
    --band: #000000;
    --accent: #9ee16f;
    --ink: #252c3a;
    --icon-tone: #2a3446;
  }
  html, body {
    margin: 0;
    padding: 0;
    overflow: hidden;
    background: var(--paper);
  }
  .slide {
    position: relative;
    width: 1200px;
    height: 675px;
    overflow: hidden;
    background: var(--paper);
    font-family: "Poppins", sans-serif;
  }
  .side-band,
  .icon-sheet {
    position: absolute;
    left: 0;
    top: 0;
    width: 1200px;
    height: 675px;
  }
  .icon-sheet {
    color: var(--icon-tone);
    fill: currentColor;
  }
  .accent-rule {
    position: absolute;
    left: 46px;
    top: 82px;
    width: 150px;
    height: 9px;
    background: var(--accent);
  }
  .slide-title {
    position: absolute;
    left: 222px;
    top: 63px;
    margin: 0;
    font-size: 34px;
    font-weight: 700;
    line-height: 1.2;
    color: var(--ink);
    letter-spacing: -0.2px;
  }
</style>
</head>
<body>
  <main class="slide">
    <svg class="side-band" viewBox="0 0 1200 675" aria-hidden="true">
      <polygon points="0,0 171,0 83,675 0,675" fill="var(--band)"/>
    </svg>
    <div class="accent-rule"></div>
    <h1 class="slide-title">Icons to use</h1>

    <svg class="icon-sheet" viewBox="0 0 1200 675" role="img" aria-label="Construction icon set: tools, machinery, cranes, hard hats, bricks, trucks, safety signs and building plans">
      <defs>
        <symbol id="i-map" viewBox="0 0 48 48"><path d="M4 10l12-4 16 4 12-4v32l-12 4-16-4-12 4z"/><path d="M16 6v32M32 10v32" stroke="#fff" stroke-width="2"/></symbol>
        <symbol id="i-gear" viewBox="0 0 48 48"><circle cx="24" cy="24" r="17" fill="none" stroke="currentColor" stroke-width="7" stroke-dasharray="6.68 6.68"/><circle cx="24" cy="24" r="15"/><circle cx="24" cy="24" r="6" fill="#fff"/></symbol>
        <symbol id="i-hammer" viewBox="0 0 48 48"><rect x="21" y="14" width="6" height="30" rx="2"/><path d="M10 6h26l4 4v6H10z"/></symbol>
        <symbol id="i-screwdriver" viewBox="0 0 48 48"><rect x="22" y="3" width="4" height="20"/><rect x="18" y="22" width="12" height="22" rx="4"/></symbol>
        <symbol id="i-wrench" viewBox="0 0 48 48"><g transform="rotate(30 24 24)"><rect x="20" y="14" width="8" height="32" rx="3"/><circle cx="24" cy="11" r="10"/><rect x="20.5" y="0" width="7" height="11" fill="#fff"/></g></symbol>
        <symbol id="i-axe" viewBox="0 0 48 48"><rect x="22" y="6" width="5" height="38" rx="2"/><path d="M8 6h16v14H8q-4-7 0-14z"/></symbol>
        <symbol id="i-roller" viewBox="0 0 48 48"><rect x="6" y="5" width="32" height="10" rx="3"/><path d="M38 10h4v12H24v7" fill="none" stroke="currentColor" stroke-width="3"/><rect x="20" y="29" width="8" height="16" rx="2"/></symbol>
        <symbol id="i-nut" viewBox="0 0 48 48"><path fill-rule="evenodd" d="M14 6h20l10 18-10 18H14L4 24zM15 24a9 9 0 1 0 18 0a9 9 0 1 0-18 0z"/></symbol>
        <symbol id="i-cone" viewBox="0 0 48 48"><path d="M20 5h8l10 33H10z"/><rect x="6" y="38" width="36" height="5" rx="1"/><path d="M16 17h16M13 28h22" stroke="#fff" stroke-width="4"/></symbol>
        <symbol id="i-excavator" viewBox="0 0 48 48"><rect x="20" y="22" width="22" height="10" rx="2"/><rect x="31" y="13" width="10" height="10"/><rect x="18" y="34" width="27" height="8" rx="4"/><path d="M22 24L12 10 6 26" fill="none" stroke="currentColor" stroke-width="4"/><path d="M1 26h11l-5 9z"/></symbol>
        <symbol id="i-bucket" viewBox="0 0 48 48"><path d="M10 18h28l-4 26H14z"/><path d="M10 18q14-18 28 0" fill="none" stroke="currentColor" stroke-width="3"/></symbol>
        <symbol id="i-brush" viewBox="0 0 48 48"><g transform="rotate(35 24 24)"><rect x="20" y="1" width="8" height="19" rx="3"/><rect x="16" y="20" width="16" height="6"/><path d="M15 26h18v17H15z"/></g></symbol>
        <symbol id="i-towercrane" viewBox="0 0 48 48"><path d="M16 44V10M22 44V10M16 14l6 6M22 20l-6 6M16 26l6 6M22 32l-6 6M3 12h43M19 3L3 12M19 3l27 9M40 12v15" fill="none" stroke="currentColor" stroke-width="2.5"/><rect x="10" y="42" width="18" height="4"/><rect x="35" y="27" width="10" height="8"/></symbol>
        <symbol id="i-hook" viewBox="0 0 48 48"><rect x="18" y="2" width="12" height="18" rx="3"/><path d="M24 20v8a8 8 0 1 1-8 8" fill="none" stroke="currentColor" stroke-width="5"/></symbol>
        <symbol id="i-plan" viewBox="0 0 48 48"><path d="M8 4h24l8 8v32H8z"/><path d="M15 28l9-8 9 8v9H15z" fill="#fff"/></symbol>
        <symbol id="i-hardhat" viewBox="0 0 48 48"><path d="M10 30a14 14 0 0 1 28 0z"/><rect x="5" y="30" width="38" height="6" rx="3"/><rect x="21" y="13" width="6" height="10" fill="#fff" opacity=".35"/></symbol>
        <symbol id="i-wheelbarrow" viewBox="0 0 48 48"><path d="M14 16h30l-6 14H20z"/><path d="M3 14h9l8 16M22 30l-2 12" fill="none" stroke="currentColor" stroke-width="3"/><circle cx="36" cy="37" r="5.5" fill="none" stroke="currentColor" stroke-width="4"/></symbol>
        <symbol id="i-brick" viewBox="0 0 48 48"><path d="M4 20l24-8 16 6v10l-24 8-16-6z"/><path d="M4 20l16 6 24-8M20 26v10" fill="none" stroke="#fff" stroke-width="2"/></symbol>
        <symbol id="i-wall" viewBox="0 0 48 48"><rect x="4" y="16" width="40" height="26"/><path d="M4 24.7h40M4 33.3h40M14 16v8.7M34 16v8.7M24 24.7v8.7M14 33.3v8.7M34 33.3v8.7" stroke="#fff" stroke-width="2"/></symbol>
        <symbol id="i-drill" viewBox="0 0 48 48"><rect x="12" y="10" width="26" height="12" rx="3"/><rect x="2" y="14" width="10" height="4"/><path d="M24 22h10l2 14H26z"/><rect x="22" y="36" width="16" height="8" rx="2"/></symbol>
        <symbol id="i-saw" viewBox="0 0 48 48"><circle cx="24" cy="21" r="15" fill="none" stroke="currentColor" stroke-width="5" stroke-dasharray="3 3"/><circle cx="24" cy="21" r="14"/><circle cx="24" cy="21" r="3" fill="#fff"/><rect x="6" y="30" width="36" height="14"/></symbol>
        <symbol id="i-warning" viewBox="0 0 48 48"><path d="M24 5L45 42H3z" fill="none" stroke="currentColor" stroke-width="3" stroke-linejoin="round"/><rect x="22" y="17" width="4" height="14" rx="1"/><circle cx="24" cy="36" r="2.5"/></symbol>
        <symbol id="i-factory" viewBox="0 0 48 48"><path d="M4 44V8h7v18l10-8v8l10-8v8l10-8v26z"/><path d="M12 34h6v6h-6zM26 34h6v6h-6z" fill="#fff"/></symbol>
        <symbol id="i-shovel" viewBox="0 0 48 48"><rect x="22" y="4" width="4" height="24"/><rect x="17" y="2" width="14" height="5" rx="2"/><path d="M16 28h16v10l-8 8-8-8z"/></symbol>
        <symbol id="i-crawlercrane" viewBox="0 0 48 48"><rect x="6" y="36" width="37" height="8" rx="4"/><rect x="24" y="23" width="17" height="13"/><path d="M26 24L10 4M31 24L15 4M13 8l14 14M11 15l11 8" fill="none" stroke="currentColor" stroke-width="2.5"/><path d="M10 4v18" stroke="currentColor" stroke-width="1.5"/><rect x="7" y="22" width="6" height="6"/></symbol>
        <symbol id="i-ladder" viewBox="0 0 48 48"><path d="M16 4v40M32 4v40M16 12h16M16 20h16M16 28h16M16 36h16" fill="none" stroke="currentColor" stroke-width="3"/></symbol>
        <symbol id="i-barrier" viewBox="0 0 48 48"><rect x="4" y="14" width="40" height="12"/><path d="M12 14l-8 12M22 14l-8 12M32 14l-8 12M42 14l-8 12" stroke="#fff" stroke-width="3"/><rect x="8" y="26" width="4" height="18"/><rect x="36" y="26" width="4" height="18"/><rect x="8" y="4" width="10" height="8" rx="2"/><rect x="30" y="4" width="10" height="8" rx="2"/></symbol>
        <symbol id="i-mixer" viewBox="0 0 48 48"><rect x="3" y="31" width="41" height="4"/><path d="M29 15h9l6 10v6H29z"/><ellipse cx="15" cy="21" rx="13" ry="9" transform="rotate(-15 15 21)"/><circle cx="10" cy="38" r="4.5" stroke="#fff" stroke-width="1.5"/><circle cx="36" cy="38" r="4.5" stroke="#fff" stroke-width="1.5"/></symbol>
        <symbol id="i-container" viewBox="0 0 48 48"><rect x="4" y="20" width="40" height="22"/><path d="M10 22v18M16 22v18M22 22v18M28 22v18M34 22v18M40 22v18" stroke="#fff" stroke-width="1.5"/><path d="M24 2v10M24 12L8 20M24 12l16 8" fill="none" stroke="currentColor" stroke-width="2"/></symbol>
        <symbol id="i-dumptruck" viewBox="0 0 48 48"><path d="M3 12h27l-2 16H5z"/><path d="M30 16h8l6 8v8H30z"/><rect x="3" y="28" width="41" height="4"/><circle cx="12" cy="37" r="5" stroke="#fff" stroke-width="1.5"/><circle cx="36" cy="37" r="5" stroke="#fff" stroke-width="1.5"/></symbol>
        <symbol id="i-tools" viewBox="0 0 48 48"><g transform="rotate(45 24 24)"><rect x="21" y="4" width="6" height="40" rx="2"/></g><g transform="rotate(-45 24 24)"><rect x="21" y="10" width="6" height="34" rx="2"/><rect x="15" y="2" width="18" height="10" rx="3"/></g></symbol>
        <symbol id="i-growth" viewBox="0 0 48 48"><path d="M4 22L20 8l16 14M8 22v20h24M10 38l10-10 6 4 16-16M35 16h7v7" fill="none" stroke="currentColor" stroke-width="3"/></symbol>
        <symbol id="i-trowel" viewBox="0 0 48 48"><g transform="rotate(-35 24 24)"><rect x="21.5" y="2" width="5" height="15" rx="2"/><rect x="23" y="16" width="2" height="9"/><path d="M10 25h28L24 44z"/></g></symbol>
        <symbol id="i-house" viewBox="0 0 48 48"><path d="M3 24L19 10l16 14h-4v16H7V24z"/><rect x="15" y="30" width="8" height="10" fill="#fff"/><path d="M41 4v28" stroke="currentColor" stroke-width="2"/><g transform="rotate(30 38 36)"><rect x="35" y="25" width="6" height="19"/></g></symbol>
      </defs>

      <!-- row 1 -->
      <use href="#i-map" x="206" y="135" width="44" height="44"/>
      <use href="#i-gear" x="279" y="135" width="44" height="44"/>
      <use href="#i-hammer" x="351" y="135" width="44" height="44"/>
      <use href="#i-hammer" x="424" y="135" width="44" height="44"/>
      <use href="#i-screwdriver" x="496" y="135" width="44" height="44"/>
      <use href="#i-screwdriver" x="569" y="135" width="44" height="44"/>
      <use href="#i-wrench" x="642" y="135" width="44" height="44"/>
      <use href="#i-axe" x="714" y="135" width="44" height="44"/>
      <use href="#i-roller" x="787" y="135" width="44" height="44"/>
      <use href="#i-nut" x="859" y="135" width="44" height="44"/>
      <use href="#i-cone" x="932" y="135" width="44" height="44"/>
      <use href="#i-excavator" x="1005" y="135" width="44" height="44"/>
      <use href="#i-bucket" x="1077" y="135" width="44" height="44"/>
      <!-- row 2 -->
      <use href="#i-excavator" x="206" y="224" width="44" height="44"/>
      <use href="#i-excavator" x="279" y="224" width="44" height="44"/>
      <use href="#i-brush" x="351" y="224" width="44" height="44"/>
      <use href="#i-towercrane" x="424" y="224" width="44" height="44"/>
      <use href="#i-hook" x="496" y="224" width="44" height="44"/>
      <use href="#i-plan" x="569" y="224" width="44" height="44"/>
      <use href="#i-hardhat" x="642" y="224" width="44" height="44"/>
      <use href="#i-axe" x="714" y="224" width="44" height="44"/>
      <use href="#i-wheelbarrow" x="787" y="224" width="44" height="44"/>
      <use href="#i-brick" x="859" y="224" width="44" height="44"/>
      <use href="#i-wall" x="932" y="224" width="44" height="44"/>
      <use href="#i-brick" x="1005" y="224" width="44" height="44"/>
      <use href="#i-hook" x="1077" y="224" width="44" height="44"/>
      <!-- row 3 -->
      <use href="#i-wrench" x="206" y="308" width="44" height="44"/>
      <use href="#i-drill" x="279" y="308" width="44" height="44"/>
      <use href="#i-drill" x="351" y="308" width="44" height="44"/>
      <use href="#i-saw" x="424" y="308" width="44" height="44"/>
      <use href="#i-gear" x="496" y="308" width="44" height="44"/>
      <use href="#i-warning" x="569" y="308" width="44" height="44"/>
      <use href="#i-factory" x="642" y="308" width="44" height="44"/>
      <use href="#i-shovel" x="714" y="308" width="44" height="44"/>
      <use href="#i-shovel" x="787" y="308" width="44" height="44"/>
      <use href="#i-crawlercrane" x="859" y="308" width="44" height="44"/>
      <use href="#i-factory" x="932" y="308" width="44" height="44"/>
      <use href="#i-ladder" x="1005" y="308" width="44" height="44"/>
      <use href="#i-barrier" x="1077" y="308" width="44" height="44"/>
      <!-- row 4 -->
      <use href="#i-mixer" x="206" y="400" width="44" height="44"/>
      <use href="#i-excavator" x="279" y="400" width="44" height="44"/>
      <use href="#i-mixer" x="351" y="400" width="44" height="44"/>
      <use href="#i-hardhat" x="424" y="400" width="44" height="44"/>
      <use href="#i-hardhat" x="496" y="400" width="44" height="44"/>
      <use href="#i-hardhat" x="569" y="400" width="44" height="44"/>
      <use href="#i-gear" x="642" y="400" width="44" height="44"/>
      <use href="#i-container" x="714" y="400" width="44" height="44"/>
      <use href="#i-crawlercrane" x="787" y="400" width="44" height="44"/>
      <use href="#i-plan" x="859" y="400" width="44" height="44"/>
      <use href="#i-factory" x="932" y="400" width="44" height="44"/>
      <use href="#i-factory" x="1005" y="400" width="44" height="44"/>
      <use href="#i-wall" x="1077" y="400" width="44" height="44"/>
      <!-- row 5 -->
      <use href="#i-wrench" x="206" y="487" width="44" height="44"/>
      <use href="#i-shovel" x="279" y="487" width="44" height="44"/>
      <use href="#i-dumptruck" x="351" y="487" width="44" height="44"/>
      <use href="#i-dumptruck" x="424" y="487" width="44" height="44"/>
      <use href="#i-roller" x="496" y="487" width="44" height="44"/>
      <use href="#i-screwdriver" x="569" y="487" width="44" height="44"/>
      <use href="#i-dumptruck" x="642" y="487" width="44" height="44"/>
      <use href="#i-wrench" x="714" y="487" width="44" height="44"/>
      <use href="#i-wrench" x="787" y="487" width="44" height="44"/>
      <use href="#i-tools" x="859" y="487" width="44" height="44"/>
      <use href="#i-shovel" x="932" y="487" width="44" height="44"/>
      <use href="#i-brush" x="1005" y="487" width="44" height="44"/>
      <use href="#i-wheelbarrow" x="1077" y="487" width="44" height="44"/>
      <!-- row 6 -->
      <use href="#i-towercrane" x="206" y="571" width="44" height="44"/>
      <use href="#i-drill" x="279" y="571" width="44" height="44"/>
      <use href="#i-hook" x="351" y="571" width="44" height="44"/>
      <use href="#i-barrier" x="424" y="571" width="44" height="44"/>
      <use href="#i-growth" x="496" y="571" width="44" height="44"/>
      <use href="#i-wheelbarrow" x="569" y="571" width="44" height="44"/>
      <use href="#i-trowel" x="642" y="571" width="44" height="44"/>
      <use href="#i-barrier" x="714" y="571" width="44" height="44"/>
      <use href="#i-house" x="787" y="571" width="44" height="44"/>
      <use href="#i-roller" x="859" y="571" width="44" height="44"/>
    </svg>
  </main>
</body>
</html>
```